Commercial Construction Company

We need a business card design based on our current logo. We are a commercial general contractor based in Southern California that specializes in bank remodels. We would like to see designs that incorporate dark blue. The final design should portray an image of professionalism and quality.

If possible, I would like to add metallic foil to the design. Thank you

```html
<!DOCTYPE html>
<html lang="en">
<head>
<meta charset="utf-8">
<title>Norvale Building Group – Business Card</title>
<link rel="stylesheet" href="https://fonts.googleapis.com/css2?family=Josefin+Sans:wght@400;600;700&display=swap">
<style>
  :root {
    --navy: #1f4479;
    --navy-deep: #1a3c6c;
    --ink: #1e1e1e;
    --rule-grey: #8a8a8a;
    --tile-1: #c8c8c8;
    --tile-2: #a9a9a9;
    --tile-3: #bcbcbc;
    --tile-4: #8e8e8e;
    --icon: #3c4f6e;
    --paper: #ffffff;
    --stage: #e6e7e9;
    --glass-a: #dfe6ea;
    --glass-b: #b9c6cf;
  }
  * { box-sizing: border-box; margin: 0; padding: 0; }
  html, body { width: 1200px; height: 689px; overflow: hidden; }
  body {
    background: var(--stage);
    font-family: "Josefin Sans", sans-serif;
    position: relative;
  }
  .card {
    position: absolute;
    top: 174px;
    width: 535px;
    height: 320px;
    border-radius: 20px;
    overflow: hidden;
    background: var(--paper);
    box-shadow: 0 6px 18px rgba(0,0,0,.12);
  }
  .card--front { left: 59px; }
  .card--back { left: 623px; }

  .glass-band {
    position: absolute;
    left: 0; right: 0;
    background: linear-gradient(90deg, var(--glass-a), var(--glass-b) 30%, var(--glass-a) 55%, var(--glass-b) 80%, var(--glass-a));
  }
  .card--front .glass-band--top { top: 0; height: 35px; }
  .card--front .glass-band--bottom { top: 286px; height: 34px; }
  .navy-rule { position: absolute; left: 0; right: 0; height: 7px; background: var(--navy); }
  .navy-rule--top { top: 35px; }
  .navy-rule--bottom { top: 279px; }

  .company-name {
    position: absolute;
    left: 0; right: 0;
    text-align: center;
    color: var(--ink);
    font-weight: 700;
    line-height: 1;
    white-space: nowrap;
  }
  .card--front .company-name { top: 136px; font-size: 30px; }
  .card--back .company-name { top: 62px; font-size: 22px; }

  .front-divider {
    position: absolute;
    left: 149px; top: 239px;
    width: 246px; height: 4px;
    background: var(--rule-grey);
  }
  .front-url {
    position: absolute;
    left: 0; right: 0; top: 257px;
    display: flex; justify-content: center; align-items: center; gap: 6px;
    color: var(--navy);
    font-size: 15px; font-weight: 600;
  }

  .card--back .glass-band--side { top: 175px; height: 145px; width: 36px; }
  .glass-band--left { left: 0; right: auto; }
  .glass-band--right { left: auto; right: 0; }
  .contact-panel {
    position: absolute;
    left: 36px; top: 175px;
    width: 462px; height: 145px;
    background: linear-gradient(180deg, var(--navy), var(--navy-deep));
  }
  .icon-bar {
    position: absolute;
    left: 163px; top: 146px;
    width: 208px; height: 56px;
    display: flex;
    border-top: 2px solid var(--navy);
    border-bottom: 2px solid var(--navy);
    padding: 2px 0;
  }
  .icon-bar__tile { flex: 1; display: flex; align-items: center; justify-content: center; }
  .icon-bar__tile:nth-child(1) { background: var(--tile-1); }
  .icon-bar__tile:nth-child(2) { background: var(--tile-2); }
  .icon-bar__tile:nth-child(3) { background: var(--tile-3); }
  .icon-bar__tile:nth-child(4) { background: var(--tile-4); }
  .contact-list {
    position: absolute;
    left: 0; right: 0; top: 217px;
    list-style: none;
    text-align: center;
    color: #fff;
    font-size: 13.5px;
    line-height: 16.2px;
  }
</style>
</head>
<body>

<section class="card card--front" aria-label="Card front">
  <div class="glass-band glass-band--top" role="img" aria-label="Soft blurred office interior photograph"></div>
  <div class="navy-rule navy-rule--top"></div>
  <p class="company-name">Norvale Building Group</p>
  <div class="front-divider"></div>
  <p class="front-url">
    <svg width="16" height="16" viewBox="0 0 16 16" fill="none" stroke="currentColor" stroke-width="1.4"><circle cx="8" cy="8" r="6.5"/><ellipse cx="8" cy="8" rx="3" ry="6.5"/><path d="M1.5 8h13"/></svg>
    www.norvalebuild.com
  </p>
  <div class="navy-rule navy-rule--bottom"></div>
  <div class="glass-band glass-band--bottom" role="img" aria-label="Soft blurred office interior photograph"></div>
</section>

<section class="card card--back" aria-label="Card back">
  <p class="company-name">Norvale Building Group</p>
  <div class="glass-band glass-band--side glass-band--left" role="img" aria-label="Soft blurred office interior photograph"></div>
  <div class="contact-panel"></div>
  <div class="glass-band glass-band--side glass-band--right" role="img" aria-label="Soft blurred office interior photograph"></div>
  <div class="icon-bar">
    <span class="icon-bar__tile"><svg width="22" height="22" viewBox="0 0 24 24" fill="none" stroke="var(--icon)" stroke-width="1.5"><path d="M5 3h4l2 5-3 2a12 12 0 0 0 6 6l2-3 5 2v4a2 2 0 0 1-2 2A17 17 0 0 1 3 5a2 2 0 0 1 2-2z"/></svg></span>
    <span class="icon-bar__tile"><svg width="24" height="22" viewBox="0 0 24 24" fill="none" stroke="var(--icon)" stroke-width="1.5"><path d="M3 10l9-7 9 7v11H3z"/><path d="M3 10l9 6 9-6"/><path d="M7 7h10M7 10h10"/></svg></span>
    <span class="icon-bar__tile"><svg width="20" height="24" viewBox="0 0 20 24" fill="none" stroke="var(--icon)" stroke-width="1.5"><path d="M10 22s7-7.5 7-13a7 7 0 0 0-14 0c0 5.5 7 13 7 13z"/><circle cx="10" cy="9" r="2.5"/></svg></span>
    <span class="icon-bar__tile"><svg width="24" height="24" viewBox="0 0 24 24" fill="none" stroke="var(--icon)" stroke-width="1.5"><circle cx="12" cy="12" r="9"/><ellipse cx="12" cy="12" rx="4" ry="9"/><path d="M3 12h18M5 7h14M5 17h14"/></svg></span>
  </div>
  <ul class="contact-list">
    <li>(555) 014-2286</li>
    <li>info@norvalebuild.com</li>
    <li>4120 Meridian Park Way Suite 310</li>
    <li>Linden Grove, CA 91800</li>
    <li>www.norvalebuild.com</li>
  </ul>
</section>

</body>
</html>
```